PSD Website Design

I am looking to have a custom website designed. I would like a PSD made of the design I came up with. Once I get the design I will slice the PSD and create a wordpress template from it.

See attachment for basic layout of the graphic. The image labeled Player page is the basic page I will need for the website. I also need a home page with an image slider on it and thumbnails of recent, state video uploads.

A textured background is ok.

Looking for a quick turnaround.

Text at top of page is a menu that is needed. Open to seeing the menu as a navigational bar or/and with different font types.

No preference on page background color or font colors. I welcome creativity.

```html
<!DOCTYPE html>
<html lang="en">
<head>
<meta charset="utf-8">
<title>Stride – Recent Videos</title>
<link rel="stylesheet" href="https://fonts.googleapis.com/css2?family=Exo+2:wght@500;700&family=Roboto+Condensed:wght@400&family=Arimo:wght@400;700&display=swap">
<style>
  :root{
    --red:#ee3f2b;
    --grey-tab:#a6a6a6;
    --ink:#1f2a2e;
    --muted:#444;
    --white:#fff;
    --grass-dark:#4c8a2a;
    --grass-light:#7fbf45;
    --panel-slate:#4d6283;
    --link:#3d5a8c;
    --panel-sky:#5aa9c9;
    --panel-pale:#dcedf7;
    --line:#d9d9d9;
    --frame:#e2e2e2;
  }
  *{box-sizing:border-box;margin:0;padding:0}
  html,body{width:1200px;height:550px;overflow:hidden}
  body{position:relative;font-family:"Roboto Condensed",sans-serif;background:var(--white)}
  .grass{position:absolute;top:0;height:512px;width:61px;background:linear-gradient(135deg,var(--grass-light),var(--grass-dark) 60%,var(--grass-light))}
  .grass.left{left:0}
  .grass.right{left:1140px}
  .page{position:absolute;left:61px;top:0;width:1079px;height:512px;background:var(--white)}
  .abs{position:absolute}

  .section-head{position:absolute;top:36px;height:35px;border-bottom:2px solid var(--red)}
  .tab{position:absolute;top:0;height:33px;font-family:"Exo 2",sans-serif;font-weight:700;font-size:19px;line-height:34px;color:var(--white);padding-left:12px;letter-spacing:.5px}
  .tab.active{background:var(--red);clip-path:polygon(0 0,88% 0,100% 100%,0 100%)}
  .tab.muted{background:var(--grey-tab);clip-path:polygon(0 0,85% 0,100% 100%,0 100%)}
  .tab.plain{color:var(--ink);font-weight:500;padding-left:0}

  .video{position:absolute;width:193px}
  .thumb{width:193px;height:113px;border:1px solid var(--frame);padding:4px;position:relative}
  .thumb .shot{width:100%;height:100%}
  .thumb svg{position:absolute;left:50%;top:50%;transform:translate(-40%,-50%)}
  .video h3{font-weight:400;font-size:14.5px;line-height:20px;color:var(--ink);margin-top:3px;padding-left:3px}
  .video time{display:block;font-size:12.5px;line-height:16px;color:var(--muted);margin-top:1px;padding-left:3px}

  .social{position:absolute;left:645px;top:93px;width:422px;height:368px;border:1px solid #c6c6c6;font-family:"Arimo",sans-serif}
  .fw-bar{height:34px;background:var(--panel-slate);color:var(--white);font-weight:400;font-size:22px;line-height:34px;padding-left:10px}
  .fw-page-pic{left:13px;top:44px;width:35px;height:35px;background:#d0d0d0;border:1px solid #bbb}
  .fw-name{left:58px;top:49px;font-size:12px;color:var(--link)}
  .fw-sub{left:58px;top:65px;font-size:10px;color:var(--link)}
  .rule{left:18px;width:360px;height:1px;background:var(--line)}
  .likes{left:30px;top:101px;font-size:9px;color:#333}
  .likes span{color:var(--link)}
  .fan{position:absolute;width:46px;text-align:center;font-size:8px;color:#666}
  .fan .pic{width:46px;height:46px;margin-bottom:5px}
  .plugin{left:22px;top:258px;font-size:8px;color:#666;display:flex;align-items:center;gap:4px}
  .plugin i{display:inline-block;width:9px;height:9px;background:var(--panel-slate)}
  .chirp-bar{left:0;top:274px;width:420px;height:35px;background:var(--panel-sky);color:var(--white);font-weight:400;font-size:22px;line-height:35px;padding-left:10px}
  .chirp-body{left:0;top:309px;width:420px;height:57px;background:var(--panel-pale)}
  .chirp-pic{left:12px;top:316px;width:41px;height:41px;background:linear-gradient(135deg,#5a1d6e,#1b0b22)}
  .chirp-name{left:63px;top:320px;font-size:12px;color:var(--link)}
  .follow{left:63px;top:337px;width:61px;height:20px;border:1px solid #b9c4cc;border-radius:3px;background:linear-gradient(#fff,#e3e8ec);font-size:11px;font-weight:700;color:#333;line-height:18px;text-align:center}

  .footer{position:absolute;left:0;top:512px;width:1200px;height:38px;background:var(--red);color:var(--white);font-family:"Arimo",sans-serif;font-size:13px;line-height:38px;text-align:center}
</style>
</head>
<body>
  <div class="grass left" role="img" aria-label="Grass texture"></div>
  <div class="grass right" role="img" aria-label="Grass texture"></div>

  <main class="page">
    <div class="section-head" style="left:14px;width:604px">
      <div class="tab muted" style="left:110px;width:124px">FLORIDA</div>
      <div class="tab active" style="left:0;width:114px">RECENT</div>
      <div class="tab plain" style="left:243px">VIDEOS</div>
    </div>

    <div class="video" style="left:14px;top:93px">
      <div class="thumb"><div class="shot" role="img" aria-label="Black and white portrait video still" style="background:linear-gradient(135deg,#555,#1e1e1e)"></div><svg width="22" height="26" viewBox="0 0 22 26"><path d="M0 0L22 13L0 26Z" fill="#fff"/></svg></div>
      <h3>How Much More Do We Evil<br>Of Black Magic</h3><time>12 Septamber 2013</time>
    </div>
    <div class="video" style="left:220px;top:93px">
      <div class="thumb"><div class="shot" role="img" aria-label="Black and white close-up video still" style="background:linear-gradient(135deg,#777,#2b2b2b)"></div><svg width="22" height="26" viewBox="0 0 22 26"><path d="M0 0L22 13L0 26Z" fill="#fff"/></svg></div>
      <h3>How Much More Do We Evil<br>Of Black Magic</h3><time>12 Septamber 2013</time>
    </div>
    <div class="video" style="left:425px;top:93px">
      <div class="thumb"><div class="shot" role="img" aria-label="Athlete torso video still" style="background:linear-gradient(180deg,#f3e4da,#cf7b4a)"></div><svg width="22" height="26" viewBox="0 0 22 26"><path d="M0 0L22 13L0 26Z" fill="#fff"/></svg></div>
      <h3>How Much More Do We Evil<br>Of Black Magic</h3><time>12 Septamber 2013</time>
    </div>
    <div class="video" style="left:14px;top:277px">
      <div class="thumb"><div class="shot" role="img" aria-label="Black and white portrait video still" style="background:linear-gradient(135deg,#555,#1e1e1e)"></div><svg width="22" height="26" viewBox="0 0 22 26"><path d="M0 0L22 13L0 26Z" fill="#fff"/></svg></div>
      <h3>How Much More Do We Evil<br>Of Black Magic</h3><time>12 Septamber 2013</time>
    </div>
    <div class="video" style="left:220px;top:277px">
      <div class="thumb"><div class="shot" role="img" aria-label="Rally car on dirt track video still" style="background:linear-gradient(180deg,#c9cdd0,#8a7458)"></div><svg width="22" height="26" viewBox="0 0 22 26"><path d="M0 0L22 13L0 26Z" fill="#fff"/></svg></div>
      <h3>How Much More Do We Evil<br>Of Black Magic</h3><time>12 Septamber 2013</time>
    </div>
    <div class="video" style="left:425px;top:277px">
      <div class="thumb"><div class="shot" role="img" aria-label="Ruined stone village at dusk video still" style="background:linear-gradient(180deg,#3d3a36,#a98457)"></div><svg width="22" height="26" viewBox="0 0 22 26"><path d="M0 0L22 13L0 26Z" fill="#fff"/></svg></div>
      <h3>How Much More Do We Evil<br>Of Black Magic</h3><time>12 Septamber 2013</time>
    </div>

    <div class="section-head" style="left:645px;width:422px">
      <div class="tab active" style="left:0;width:172px">TAKE IT VIRAL</div>
    </div>

    <aside class="social">
      <div class="fw-bar">Friendwall</div>
      <div class="abs fw-page-pic"></div>
      <div class="abs fw-name">Athletic recruiting</div>
      <div class="abs fw-sub">on Friendwall</div>
      <div class="abs rule" style="top:94px"></div>
      <div class="abs likes">5,000 people like <span>this page</span></div>

      <div class="fan" style="left:21px;top:117px"><div class="pic" role="img" aria-label="Fan photo" style="background:#8a6d55"></div>Liam</div>
      <div class="fan" style="left:72px;top:117px"><div class="pic" role="img" aria-label="Fan photo" style="background:#7fa7c4"></div>Theo</div>
      <div class="fan" style="left:123px;top:117px"><div class="pic" role="img" aria-label="Fan avatar" style="background:#d9d24a"></div>Sadie</div>
      <div class="fan" style="left:174px;top:117px"><div class="pic" role="img" aria-label="Fan photo" style="background:#4b4f5a"></div>Jonah</div>
      <div class="fan" style="left:225px;top:117px"><div class="pic" role="img" aria-label="Fan photo" style="background:#b8655a"></div>Malakai</div>
      <div class="fan" style="left:276px;top:117px"><div class="pic" role="img" aria-label="Fan photo" style="background:#b8655a"></div>Jonah</div>
      <div class="fan" style="left:327px;top:117px"><div class="pic" role="img" aria-label="Fan photo" style="background:#b8655a"></div>Malakai</div>

      <div class="fan" style="left:21px;top:185px"><div class="pic" role="img" aria-label="Fan photo" style="background:#9a9a9a"></div>Dario</div>
      <div class="fan" style="left:72px;top:185px"><div class="pic" role="img" aria-label="Fan photo" style="background:#d88a8a"></div>Mina</div>
      <div class="fan" style="left:123px;top:185px"><div class="pic" role="img" aria-label="Fan photo" style="background:#b79ab0"></div>Maren</div>
      <div class="fan" style="left:174px;top:185px"><div class="pic" role="img" aria-label="Fan photo" style="background:#1f6d5e"></div>Cyril</div>
      <div class="fan" style="left:225px;top:185px"><div class="pic" role="img" aria-label="Fan photo" style="background:#5b6b5d"></div>Beata</div>
      <div class="fan" style="left:276px;top:185px"><div class="pic" role="img" aria-label="Fan photo" style="background:#1f6d5e"></div>Cyril</div>
      <div class="fan" style="left:327px;top:185px"><div class="pic" role="img" aria-label="Fan photo" style="background:#5b6b5d"></div>Beata</div>

      <div class="abs rule" style="top:252px"></div>
      <div class="abs plugin"><i></i>Friendwall social plugin</div>

      <div class="abs chirp-bar">Chirpline</div>
      <div class="abs chirp-body"></div>
      <div class="abs chirp-pic" role="img" aria-label="Profile avatar"></div>
      <div class="abs chirp-name">Athletic recruiting on Chirpline</div>
      <div class="abs follow">Follow</div>
    </aside>
  </main>

  <footer class="footer">Stride 2015 @ All Rights Reserved</footer>
</body>
</html>
```